Hollow Lantern Distillery

I need a label designed for my small distillery. I’d like it to have a rose, and the name hollow lantern in script writing. I need the graphic to fit a standard gin bottle and I’ll need to be able to edit it depending on alcohol, warning and descriptions. I want it to look elegant and attractive, but slightly daring too. It’s a 700ml oslo bottle
Target Market(s)
Bespoke gin and vodka drinkers
Industry/Entity Type
Beverage
Font styles to use
Script
Other font styles liked:
- Something easy to read
Requirements
Must have
- Room for me to add and remove text depending on the drink
Nice to have
- Hollow lantern in script, slight colour on the rose and black writing

```html
<!DOCTYPE html>
<html lang="en">
<head>
<meta charset="utf-8">
<title>Hollow Lantern Distillery – Label Range</title>
<link href="https://fonts.googleapis.com/css2?family=Libre+Bodoni:wght@400;700&display=swap" rel="stylesheet">
<style>
  :root {
    --ink: #141414;
    --paper: #ffffff;
    --silver-light: #f1f1f1;
    --silver-mid: #c9c9c9;
    --silver-deep: #a9a9a9;
    --rose: #eeb3ad;
    --serif: "Libre Bodoni", "Bodoni Moda", Georgia, serif;
  }
  * { box-sizing: border-box; margin: 0; padding: 0; }
  html, body { width: 1200px; height: 1200px; overflow: hidden; background: var(--paper); }
  .board { position: relative; width: 1200px; height: 1200px; background: var(--paper); font-family: var(--serif); color: var(--ink); }

  .label {
    position: absolute;
    width: 23.1em;
    height: 29.4em;
    border: 0.35em solid var(--ink);
    background: var(--paper);
    padding: 0.55em;
  }
  .label--left   { left: 136px; top: 331px; font-size: 10px; }
  .label--center { left: 484px; top: 318px; font-size: 8.9px; }
  .label--right  { left: 813px; top: 331px; font-size: 10px; }

  .label__panel {
    position: relative;
    width: 100%;
    height: 100%;
    border: 0.13em solid var(--ink);
    background:
      linear-gradient(158deg, var(--silver-light) 0 38%, transparent 38.2%),
      linear-gradient(90deg, var(--silver-deep) 0%, #e6e6e6 35%, var(--silver-mid) 60%, #f0f0f0 80%, var(--silver-deep) 100%);
  }
  .label__mark {
    position: absolute;
    left: 50%;
    top: 3.2em;
    width: 2.6em;
    height: 2.6em;
    margin-left: -1.3em;
    border-radius: 50%;
    background: var(--rose);
  }
  .label__brand {
    position: absolute;
    left: 0; right: 0;
    top: 7.6em;
    text-align: center;
    font-size: 1.5em;
    font-weight: 400;
    color: var(--ink);
  }
  .label__tagline {
    position: absolute;
    left: 0; right: 0;
    top: 16em;
    text-align: center;
    font-size: 0.95em;
  }
  .label__spirit {
    position: absolute;
    left: 0; right: 0;
    top: 4.05em;
    text-align: center;
    font-size: 4.2em;
    font-weight: 400;
    line-height: 1;
    letter-spacing: 0.01em;
  }
  .label__spirit--bold { font-weight: 700; font-size: 3.9em; top: 4.4em; }
  .label__volume {
    position: absolute;
    left: 0; right: 0;
    bottom: 1.1em;
    text-align: center;
    font-size: 0.95em;
  }

  .brandmark {
    position: absolute;
    left: 0; right: 0;
    top: 880px;
    text-align: center;
  }
  .brandmark__dot {
    display: block;
    width: 70px;
    height: 70px;
    margin: 0 auto 24px;
    border-radius: 50%;
    background: var(--rose);
  }
  .brandmark__name {
    font-size: 92px;
    font-weight: 400;
    line-height: 1;
    color: var(--ink);
  }
</style>
</head>
<body>
<main class="board">

  <article class="label label--left">
    <div class="label__panel">
      <span class="label__mark"></span>
      <p class="label__brand">Hollow Lantern</p>
      <p class="label__tagline">hand crafted</p>
      <h2 class="label__spirit">GIN</h2>
      <p class="label__volume">41.8% Alc. / 700ml vol.</p>
    </div>
  </article>

  <article class="label label--center">
    <div class="label__panel">
      <span class="label__mark"></span>
      <p class="label__brand">Hollow Lantern</p>
      <p class="label__tagline">hand crafted</p>
      <h2 class="label__spirit">GIN</h2>
      <p class="label__volume">41.8% Alc. / 700ml vol.</p>
    </div>
  </article>

  <article class="label label--right">
    <div class="label__panel">
      <span class="label__mark"></span>
      <p class="label__brand">Hollow Lantern</p>
      <p class="label__tagline">hand crafted</p>
      <h2 class="label__spirit label__spirit--bold">VODKA</h2>
      <p class="label__volume">41.8% Alc. / 700ml vol.</p>
    </div>
  </article>

  <section class="brandmark">
    <span class="brandmark__dot"></span>
    <h1 class="brandmark__name">Hollow Lantern</h1>
  </section>

</main>
</body>
</html>
```